Business Card Design

I want something very modern, Im from the gold coast Australia double sided and using my attached logo, a mix of cameras or a close up, I will attach pics, no logo please from other manufacturers, only Guard Every Nook, I want to promote a individual approach to security, My logo is - Honest Advise Without The Price - :)

Target Market(s)

Anyone that handles money or wants to secure there premises

Industry/Entity Type

Business

Contact Information for Business Card

Marcus Dale finch
Guard Every Nook
Coralbrook Queensland 4218
Mobile : 0431 587 902 & Skype +610431587902
Security Provider Licence QLD - 5829143
Free Quotes
CCTV, Alarms, Digital Cameras, RFID, - In Home Design

Colors

Designer to choose colors to be used in the design.

Requirements
Must have
• Free Quotes
On Site Design
Full details And Licence number Etc
Should not have
• I know these are low res pics, im waiting to receive stock before taking new photos

```html
<!DOCTYPE html>
<html lang="en">
<head>
<meta charset="utf-8">
<title>Guard Every Nook – Business Card</title>
<link href="https://fonts.googleapis.com/css2?family=Roboto+Condensed:ital,wght@0,400;0,700;1,400&display=swap" rel="stylesheet">
<style>
  :root {
    --paper: #ffffff;
    --ink: #111111;
    --muted: #8a8a8a;
    --rule: #9a9a9a;
    --band: #8c8c8c;
    --crop: #222222;
    --night-deep: #0d1f33;
    --night-mid: #24506e;
    --city-glow: #c4682a;
    --panel: rgba(40, 86, 120, 0.55);
    --white: #ffffff;
  }
  * { margin: 0; padding: 0; box-sizing: border-box; }
  html, body {
    width: 1200px; height: 470px; overflow: hidden;
    background: var(--paper);
    font-family: "Roboto Condensed", "Arial Narrow", sans-serif;
  }
  .sheet { position: relative; width: 1200px; height: 470px; }
  .crop-marks { position: absolute; inset: 0; }
  .crop-marks line { stroke: var(--crop); stroke-width: 0.8; }

  .card { position: absolute; top: 79px; width: 489px; height: 312px; }
  .card--front { left: 79px; background: var(--paper); }
  .card--back { left: 633px; overflow: hidden; }

  .product-photo {
    position: absolute; left: 37px; top: 41px; width: 107px; height: 62px;
    background: linear-gradient(135deg, #f2f2f2, #c9ccd0 60%, #9aa0a6);
    border-radius: 4px;
  }
  .tagline {
    position: absolute; right: 42px; top: 50px;
    font-size: 22px; font-weight: 700; color: var(--muted); white-space: nowrap;
  }
  .licence {
    position: absolute; right: 44px; top: 83px;
    font-size: 13px; font-style: italic; color: var(--ink); white-space: nowrap;
  }
  .header-rule {
    position: absolute; left: 39px; top: 107px; width: 410px; height: 2px;
    background: var(--rule);
  }
  .brand {
    position: absolute; left: 66px; top: 216px;
    display: flex; align-items: center; gap: 7px;
    font-size: 18px; font-weight: 700; color: var(--ink); white-space: nowrap;
  }
  .brand-mark { width: 11px; height: 11px; background: var(--ink); flex: none; }

  .contact { position: absolute; left: 259px; top: 127px; color: var(--ink); }
  .contact-name { font-size: 21px; font-weight: 700; line-height: 1.2; }
  .contact-role { font-size: 13px; line-height: 1.3; margin-bottom: 12px; }
  .contact-line { font-size: 15px; line-height: 1.35; white-space: pre; }

  .service-band {
    position: absolute; left: 0; bottom: 0; width: 100%; height: 38px;
    background: var(--band); color: var(--white);
    display: flex; align-items: center; justify-content: center;
    font-size: 12px; font-weight: 700;
  }

  .city-photo {
    position: absolute; inset: 0;
    background:
      radial-gradient(ellipse 55% 50% at 70% 85%, var(--city-glow), transparent 70%),
      linear-gradient(180deg, var(--night-deep) 0%, var(--night-mid) 30%, #1b3a52 60%, #3a3a40 100%);
  }
  .services-panel {
    position: absolute; left: 54px; top: 37px; width: 207px; height: 238px;
    background: var(--panel); list-style: none; padding: 17px 0 0 16px;
  }
  .services-panel li {
    display: flex; align-items: center; gap: 11px;
    font-size: 20px; font-weight: 700; color: var(--white);
    height: 36.3px;
  }
  .services-panel li::before {
    content: ""; width: 6px; height: 6px; background: var(--white); flex: none;
  }
</style>
</head>
<body>
<div class="sheet">
  <svg class="crop-marks" width="1200" height="470" viewBox="0 0 1200 470" aria-hidden="true">
    <line x1="94" y1="0" x2="94" y2="62"/><line x1="552" y1="0" x2="552" y2="62"/>
    <line x1="647" y1="0" x2="647" y2="62"/><line x1="1106" y1="0" x2="1106" y2="62"/>
    <line x1="94" y1="407" x2="94" y2="470"/><line x1="552" y1="407" x2="552" y2="470"/>
    <line x1="647" y1="407" x2="647" y2="470"/><line x1="1106" y1="407" x2="1106" y2="470"/>
    <line x1="0" y1="94" x2="62" y2="94"/><line x1="0" y1="377" x2="62" y2="377"/>
    <line x1="554" y1="94" x2="617" y2="94"/><line x1="554" y1="377" x2="617" y2="377"/>
    <line x1="583" y1="94" x2="645" y2="94"/><line x1="583" y1="377" x2="645" y2="377"/>
    <line x1="1138" y1="94" x2="1200" y2="94"/><line x1="1138" y1="377" x2="1200" y2="377"/>
  </svg>

  <section class="card card--front">
    <div class="product-photo" role="img" aria-label="White bullet CCTV camera on a wall bracket"></div>
    <div class="tagline">Honest Advice Without The Price</div>
    <div class="licence">Security Provider Licence QLD - 5829143</div>
    <div class="header-rule"></div>
    <div class="brand"><span class="brand-mark"></span>Guard Every Nook</div>
    <div class="contact">
      <div class="contact-name">Marcus Dale Finch</div>
      <div class="contact-role">Security Consultant</div>
      <div class="contact-line">Coralbrook Queensland 4218</div>
      <div class="contact-line">Mobile  : 0431 587 902</div>
      <div class="contact-line">Skype   : +610431587902</div>
    </div>
    <div class="service-band">Free Quotes - CCTV Alarms Megapixel Cameras RFID - Onsite Design</div>
  </section>

  <section class="card card--back">
    <div class="city-photo" role="img" aria-label="Night aerial view of a coastal city skyline and beach with bullet, dome and PTZ security cameras"></div>
    <ul class="services-panel">
      <li>Free Quotes</li>
      <li>CCTV</li>
      <li>Digital Cameras</li>
      <li>RFID</li>
      <li>Intercoms</li>
      <li>Onsite Design</li>
    </ul>
  </section>
</div>
</body>
</html>
```